Computer repair shop

A card with our logo. And number and email and address. Our colors are baby /light blue and gray

Prefferably one sode with full logo - interested in other designs and options

Computer / laptop repair shop
On site support
Snall business IT support

```html
<!DOCTYPE html>
<html lang="en">
<head>
<meta charset="utf-8">
<title>Bytewise Repair – Business Card</title>
<link href="https://fonts.googleapis.com/css2?family=Montserrat:wght@600&family=Lato:wght@400&display=swap" rel="stylesheet">
<style>
  :root {
    --page-bg: #e9eaec;
    --card-bg: #ffffff;
    --brand-blue: #2a9fd8;
    --ink: #1c1c1c;
    --accent-red: #e3262d;
    --band-dark: #0d0d0d;
  }
  html, body {
    margin: 0;
    width: 1200px;
    height: 1200px;
    overflow: hidden;
    background: var(--page-bg);
  }
  .canvas {
    position: relative;
    width: 1200px;
    height: 1200px;
  }
  .card {
    position: absolute;
    left: 215px;
    width: 770px;
    height: 440px;
    background: var(--card-bg);
    box-shadow: 0 6px 18px rgba(0,0,0,0.18);
    overflow: hidden;
  }
  .card--front { top: 130px; }
  .card--back { top: 622px; }

  .card__band {
    position: absolute;
    left: 0; right: 0; bottom: 0;
    height: 14px;
  }
  .card--front .card__band { background: var(--brand-blue); }
  .card--back .card__band { background: var(--band-dark); }

  .person__name {
    position: absolute;
    left: 61px; top: 64px;
    margin: 0;
    font-family: "Montserrat", sans-serif;
    font-weight: 600;
    font-size: 29px;
    letter-spacing: -0.3px;
    color: var(--brand-blue);
  }
  .person__role {
    position: absolute;
    left: 61px; top: 106px;
    margin: 0;
    font-family: "Lato", sans-serif;
    font-size: 18px;
    letter-spacing: 0.6px;
    color: var(--ink);
  }

  .brand-name {
    position: absolute;
    margin: 0;
    font-family: "Montserrat", sans-serif;
    font-weight: 600;
    color: var(--ink);
    line-height: 1.05;
    display: flex;
    align-items: center;
  }
  .brand-name__dot {
    display: inline-block;
    border-radius: 50%;
    background: var(--brand-blue);
    flex: none;
  }
  .card--front .brand-name {
    left: 61px; top: 232px;
    font-size: 32px;
    gap: 14px;
  }
  .card--front .brand-name__dot { width: 40px; height: 40px; }
  .card--back .brand-name {
    left: 0; right: 0; top: 150px;
    justify-content: center;
    font-size: 54px;
    gap: 22px;
  }
  .card--back .brand-name__dot { width: 64px; height: 64px; }

  .divider {
    position: absolute;
    left: 384px; top: 245px;
    width: 2px; height: 114px;
    background: var(--ink);
  }

  .contact {
    position: absolute;
    left: 435px; top: 236px;
    margin: 0; padding: 0;
    list-style: none;
    font-family: "Lato", sans-serif;
    font-size: 18px;
    color: var(--ink);
  }
  .contact__item {
    display: flex;
    align-items: center;
    height: 32px;
  }
  .contact__icon {
    width: 16px; height: 16px;
    margin-right: 10px;
    flex: none;
  }
  .contact__item--plain { margin-bottom: 4px; }

  .services {
    position: absolute;
    left: 48px; right: 40px; top: 384px;
    margin: 0; padding: 0;
    list-style: none;
    display: flex;
    gap: 26px;
    font-family: "Lato", sans-serif;
    font-size: 18px;
    color: var(--ink);
  }
  .services__item {
    display: flex;
    align-items: center;
    white-space: nowrap;
  }
  .services__item::before {
    content: "";
    width: 9px; height: 9px;
    border-radius: 50%;
    background: var(--accent-red);
    margin-right: 10px;
  }
</style>
</head>
<body>
<main class="canvas">

  <section class="card card--front" aria-label="Business card front">
    <h1 class="person__name">DANIEL HARPER</h1>
    <p class="person__role">Founder &amp; CEO</p>

    <p class="brand-name"><span class="brand-name__dot"></span>Bytewise<br>Repair</p>

    <div class="divider"></div>

    <ul class="contact">
      <li class="contact__item contact__item--plain">London, UK</li>
      <li class="contact__item">
        <svg class="contact__icon" viewBox="0 0 16 16" aria-hidden="true">
          <rect x="4" y="1" width="8" height="14" rx="1.5" fill="none" stroke="var(--accent-red)" stroke-width="1.8"/>
          <circle cx="8" cy="12.3" r="0.9" fill="var(--accent-red)"/>
        </svg>000 000 0000
      </li>
      <li class="contact__item">
        <svg class="contact__icon" viewBox="0 0 16 16" aria-hidden="true">
          <rect x="1" y="3.5" width="14" height="10" rx="1" fill="var(--accent-red)"/>
          <path d="M1.5 4.5 L8 9.5 L14.5 4.5" fill="none" stroke="#fff" stroke-width="1.2"/>
        </svg>d_harper@bytewiserepair.com
      </li>
      <li class="contact__item">
        <svg class="contact__icon" viewBox="0 0 16 16" aria-hidden="true">
          <g fill="none" stroke="var(--accent-red)" stroke-width="1.3">
            <circle cx="8" cy="8" r="6.5"/>
            <ellipse cx="8" cy="8" rx="2.8" ry="6.5"/>
            <line x1="1.5" y1="8" x2="14.5" y2="8"/>
            <line x1="2.5" y1="4.8" x2="13.5" y2="4.8"/>
            <line x1="2.5" y1="11.2" x2="13.5" y2="11.2"/>
          </g>
        </svg>www.bytewiserepair.com
      </li>
    </ul>

    <div class="card__band"></div>
  </section>

  <section class="card card--back" aria-label="Business card back">
    <p class="brand-name"><span class="brand-name__dot"></span>Bytewise Repair</p>

    <ul class="services">
      <li class="services__item">Computer / laptop repair shop</li>
      <li class="services__item">On site support</li>
      <li class="services__item">Snall business IT support</li>
    </ul>

    <div class="card__band"></div>
  </section>

</main>
</body>
</html>
```